Natural Immune System Booster

We need a pharmaceutical type box and label design for a vitamin supplement product. Korvelix is in process of being trademarked and should therefore carry the TM symbol. It is comprised of a special blend of over 20 vitamins, herbs and minerals with a High strength vitamin C booster. The tag line should read. The No.1 Natural Support For Your Immune System. Each tube contains 10 tablets. A bar code will be placed on the box carton. We prefer bright and vivid colours, preferably a mix of electric purple, yellow and orange mix. We have three flavours, summer berry (strawberry), tropical fruit and juicy orange - the box and label should indicate the flavours in a creative design element. Effervescent tabelts should be clearly marked on the box and label. The ingredients and instructions should be present on the box outer carton and also the label. We require an eye catching yet simple and bright design that pops off the shelf.
Updates

Target Market(s)

Target customers are male and female 20 - 60+ that live in Western countries that handle household budgets.

Industry/Entity Type

Pharmaceutical

Requirements
Must have
• Please see current box design, all necessary elements and specifications are included here. We require same to be placed on new design.

I have attached a txt file of the supplement facts and other details that are required for both the label and the box

```html
<!DOCTYPE html>
<html lang="en">
<head>
<meta charset="utf-8">
<title>Korvelix Effervescent Tablets – Carton Dieline</title>
<link rel="stylesheet" href="https://fonts.googleapis.com/css2?family=Source+Sans+3:wght@400;600;700;900&family=PT+Sans+Narrow:wght@400;700&display=swap">
<style>
  :root{
    --bg-dark:#1a1a1a;
    --bg-mid:#5a5a5a;
    --panel:#ffffff;
    --fold:#c9c9c9;
    --brand-red:#be1e2d;
    --deep-red:#8e1420;
    --pill-blue:#2ea7e0;
    --pill-navy:#2b3990;
    --ink:#1a1a1a;
    --purple:#4b2a7b;
    --orange:#f7941d;
    --yellow:#f2e600;
  }
  *{box-sizing:border-box;margin:0;padding:0}
  html,body{width:1200px;height:999px;overflow:hidden}
  body{
    position:relative;
    background:radial-gradient(ellipse at 50% 45%,var(--bg-mid) 0%,#333 55%,var(--bg-dark) 100%);
    font-family:"Source Sans 3",Arial,sans-serif;
    color:var(--ink);
  }
  .dieline{position:absolute;left:0;top:0}
  .abs{position:absolute}

  /* Front face */
  .brand-name{
    font-weight:700;color:var(--brand-red);font-size:66px;line-height:1;letter-spacing:-1px;
    font-family:"Source Sans 3",Arial,sans-serif;
  }
  .tm{font-size:14px;font-weight:400;color:var(--ink)}
  .tagline{font-size:12.5px;font-weight:600;letter-spacing:-.2px}
  .eff-pill{
    background:var(--pill-blue);color:#fff;border-radius:12px;
    font-size:15.5px;font-weight:600;text-align:center;line-height:22px;width:171px;height:22px;
  }
  .front-copy{font-size:14.5px;line-height:20px;text-align:center;width:190px}
  .count-badge{
    width:76px;height:70px;display:flex;flex-direction:column;align-items:center;justify-content:center;
    font-weight:700;line-height:1;color:var(--ink)
  }
  .count-badge b{font-size:19px}
  .count-badge span{font-size:14px}

  /* Side faces */
  .side-name{font-weight:700;color:var(--brand-red);font-size:44px;white-space:nowrap;line-height:1}
  .side-name .tm{font-size:10px}

  /* Back face */
  .back-heading{font-size:16px;font-weight:700;line-height:20px;width:400px}
  .red-bar{
    height:27px;background:linear-gradient(#c8202f,var(--deep-red));color:#fff;
    font-weight:700;font-size:15.5px;line-height:27px;
  }
  .blue-strip{
    background:linear-gradient(90deg,var(--pill-blue),var(--pill-navy));color:#fff;
    font-size:9.5px;font-weight:600;border-radius:12px;height:22px;line-height:22px;padding-left:10px;width:344px
  }
  .batch{font-size:13px;font-weight:700}
  .dose-star{font-size:11px;font-weight:700;color:#fff;text-align:center;line-height:12px;width:70px}

  /* Facts panel (rotated) */
  .facts{
    width:183px;height:434px;transform:rotate(-90deg);transform-origin:center;
    left:458px;top:-59px;border:3px solid #000;padding:4px 5px;font-size:6.4px;line-height:1.2;
    font-family:"PT Sans Narrow",Arial,sans-serif;
  }
  .facts h2{font-family:"Source Sans 3",Arial,sans-serif;font-size:17px;font-weight:900;line-height:1;border-bottom:1px solid #000;padding-bottom:2px}
  .facts table{width:100%;border-collapse:collapse}
  .facts td{border-bottom:.6px solid #000;padding:1.5px 0;vertical-align:top}
  .facts td.num{text-align:right;white-space:nowrap;padding-left:3px}
  .facts .thick td{border-bottom:3px solid #000}
  .facts h3{font-size:7.4px;font-weight:700;margin-top:3px}
  .facts p{border-bottom:.6px solid #000;padding-bottom:2px}
  .info-col{
    width:183px;height:115px;transform:rotate(-90deg);transform-origin:center;
    left:735px;top:101px;font-size:5.8px;line-height:1.25;font-family:"PT Sans Narrow",Arial,sans-serif;
  }
  .info-col p{margin-bottom:4px}
</style>
</head>
<body>

<svg class="dieline" width="1200" height="999" viewBox="0 0 1200 999" xmlns="http://www.w3.org/2000/svg">
  <defs>
    <linearGradient id="artFront" x1="0" y1="0" x2="1" y2="1">
      <stop offset="0" stop-color="#f2e600"/>
      <stop offset=".3" stop-color="#4b2a7b"/>
      <stop offset=".6" stop-color="#f7941d"/>
      <stop offset="1" stop-color="#e8452c"/>
    </linearGradient>
    <linearGradient id="artSide" x1="0" y1="0" x2="1" y2="1">
      <stop offset="0" stop-color="#f2e600"/>
      <stop offset=".35" stop-color="#4b2a7b"/>
      <stop offset=".7" stop-color="#f26522"/>
      <stop offset="1" stop-color="#be1e2d"/>
    </linearGradient>
    <linearGradient id="backWash" x1="0" y1="0" x2="1" y2="0">
      <stop offset="0" stop-color="#f6f6f6"/>
      <stop offset=".5" stop-color="#ffffff"/>
      <stop offset="1" stop-color="#f0f0f0"/>
    </linearGradient>
  </defs>

  <g fill="#ffffff" stroke="#bdbdbd" stroke-width="1">
    <!-- top dust flaps -->
    <path d="M310 88 L228 88 Q215 90 215 100 L238 262 L310 262 Z"/>
    <path d="M890 88 L972 88 Q985 90 985 100 L962 262 L890 262 Z"/>
    <!-- facts panel -->
    <path d="M310 262 L310 60 Q312 48 330 48 L870 48 Q888 48 890 60 L890 262 Z"/>
    <!-- left side panel -->
    <path d="M97 262 L310 262 L310 470 L78 470 Z"/>
    <!-- front panel -->
    <rect x="310" y="262" width="580" height="208"/>
    <!-- middle flaps -->
    <path d="M310 470 L238 470 L215 683 L310 683 Z"/>
    <!-- back panel -->
    <rect x="310" y="470" width="605" height="213" fill="url(#backWash)"/>
    <!-- right side panel -->
    <path d="M915 470 L1103 470 L1120 683 L915 683 Z"/>
    <!-- lower front panel -->
    <rect x="310" y="683" width="580" height="212"/>
    <!-- bottom flaps -->
    <path d="M890 683 L962 683 L985 862 L890 862 Z"/>
    <path d="M310 895 L890 895 L872 952 L328 952 Z"/>
  </g>

  <g role="img" aria-label="Abstract shard artwork in yellow, electric purple, orange and red">
    <polygon points="620,262 890,262 890,470 540,470 600,330" fill="url(#artFront)"/>
  </g>
  <g role="img" aria-label="Abstract shard artwork in yellow, electric purple, orange and red">
    <polygon points="620,683 890,683 890,895 540,895 600,755" fill="url(#artFront)"/>
  </g>
  <g role="img" aria-label="Abstract shard artwork in purple, orange and red">
    <polygon points="97,262 235,262 200,470 78,470" fill="url(#artSide)"/>
  </g>
  <g role="img" aria-label="Abstract shard artwork in purple, orange and red">
    <polygon points="965,470 1103,470 1120,683 1000,683" fill="url(#artSide)"/>
  </g>

  <!-- count badges -->
  <polygon points="815,380 855,380 875,415 855,450 815,450 795,415" fill="#fff"/>
  <polygon points="815,804 855,804 875,839 855,874 815,874 795,839" fill="#fff"/>

  <!-- dose starburst -->
  <polygon fill="#a3121f" points="835,477 846,488 862,484 865,499 880,505 873,519 880,534 865,540 862,555 846,551 835,562 824,551 808,555 805,540 790,534 797,519 790,505 805,499 808,484 824,488"/>
  <!-- red bar divider -->
  <polygon points="437,580 448,553 456,553 445,580" fill="#fff"/>
</svg>

<!-- Facts panel -->
<section class="abs facts" aria-label="Supplement facts">
  <h2>SUPPLEMENT FACTS</h2>
  <table>
    <tr><td>Serving size 1 tablet</td><td class="num">% DV</td></tr>
    <tr><td>Each serving contains</td><td class="num"></td></tr>
    <tr class="thick"><td>Calories</td><td class="num">3</td></tr>
    <tr><td>Vitamin A (Retinyl Acetate) 2100IU</td><td class="num">41%</td></tr>
    <tr><td>Vitamin C (As Ascorbic Acid) 1050mg</td><td class="num">1670%</td></tr>
    <tr><td>Vitamin E (As d-alpha tocopheryl) 20IU</td><td class="num">100%</td></tr>
    <tr><td>Riboflavin (As Riboflavin) 3.00mg</td><td class="num">135%</td></tr>
    <tr><td>Zinc (As Sulphate) 10mg</td><td class="num">65%</td></tr>
    <tr><td>Magnesium (As Oxide and Sulphate) 40mg</td><td class="num">10%</td></tr>
    <tr><td>Selenium (As Selenium enriched yeast) 15mcg</td><td class="num">22%</td></tr>
    <tr><td>Manganese (As Sulphate) 5mg</td><td class="num">250%</td></tr>
    <tr><td>Sodium (As Bicarbonate) 310mg</td><td class="num">10.5%</td></tr>
    <tr class="thick"><td>Potassium (As Bicarbonate) 125mg</td><td class="num">3%</td></tr>
  </table>
  <h3>Proprietary Herbal Blend: (400mg*)</h3>
  <p>Lonicera Japonica (Flower), Forsythia Suspensa (Fruit), Echinacea purpurea (Aerial), Astragalus (Root), Ganoderma Lucidum, Ginger (Root), Olive Leaf, Elder (Berry).</p>
  <h3>Proprietary Amino Acid Blend (50mg*)</h3>
  <p>Glutamine as L-Glutamine, Lysine as L-Lysine HCl</p>
  <h3>Proprietary Amino Acid Blend (50mg*)</h3>
  <p>Glutamine as L-Glutamine, Lysine as L-Lysine HCl</p>
  <h3>Other Ingredients:</h3>
  <p>Sucrose, Maltodextrin, Citric acid, Artificial flavor, Sucralose, Natural Color.</p>
</section>

<section class="abs info-col" aria-label="Directions and distributor">
  <p>Directions: For adults and children over 12, dissolve one tablet in a glass of water. Take up to three times per day. Do not exceed stated dose. Consult your doctor if pregnant.</p>
  <p>*Daily values not established. Percent Daily Values are based on a 2,000 calorie diet.</p>
  <p>Distributed by Korvelix LLC, 4820 Harbor Lane, Example County, USA.<br>Email: info@korvelix.example &nbsp; web: www.korvelix.example &nbsp; tel: 1-800-555-0142</p>
</section>

<!-- Front panel -->
<div class="abs brand-name" style="left:328px;top:278px">Korvelix</div>
<div class="abs tm" style="left:626px;top:275px">TM</div>
<div class="abs tagline" style="left:332px;top:342px">The No.1 Natural Support For Your Immune Systemt</div>
<div class="abs eff-pill" style="left:337px;top:372px">Effervescent tablets</div>
<div class="abs front-copy" style="left:329px;top:405px">Boost of Vitamin C with over 20 Herbs, Minerals and Vitamins.</div>
<div class="abs count-badge" style="left:797px;top:380px"><b>10</b><span>tablets</span></div>

<!-- Lower front panel -->
<div class="abs brand-name" style="left:328px;top:700px">Korvelix</div>
<div class="abs tm" style="left:626px;top:699px">TM</div>
<div class="abs tagline" style="left:332px;top:765px">The No.1 Natural Support For Your Immune Systemt</div>
<div class="abs eff-pill" style="left:337px;top:795px">Effervescent tablets</div>
<div class="abs front-copy" style="left:329px;top:828px">Boost of Vitamin C with over 20 Herbs, Minerals and Vitamins.</div>
<div class="abs count-badge" style="left:797px;top:804px"><b>10</b><span>tablets</span></div>

<!-- Left side panel -->
<div class="abs side-name" style="left:188px;top:344px;transform:rotate(90deg);transform-origin:center">Korvelix<span class="tm">TM</span></div>

<!-- Right side panel -->
<div class="abs side-name" style="left:856px;top:555px;transform:rotate(-90deg);transform-origin:center">Korvelix<span class="tm">TM</span></div>

<!-- Back panel -->
<div class="abs back-heading" style="left:331px;top:504px">Created by an Engineer and designed to be The No.1 Natural Support For Your Immune System*</div>
<div class="abs red-bar" style="left:330px;top:553px;width:118px;padding-left:14px">10 Tablets</div>
<div class="abs red-bar" style="left:445px;top:553px;width:243px;padding-left:20px">Replace Cap After Opening</div>
<div class="abs blue-strip" style="left:328px;top:605px">Boost of High Strenght Vitamin C with over 20 Herbs, Vitamins and Minerals.</div>
<div class="abs batch" style="left:720px;top:546px">Lot No.</div>
<div class="abs batch" style="left:720px;top:571px">Expiry Date:</div>
<div class="abs dose-star" style="left:800px;top:502px">Take Up to 3 Times Per Day.</div>

</body>
</html>
```